Tree company needs modern website design

We need a website design for a tree company, here are some websites they like:

http://harborvantage.com/company/ - we like the big image filling most of the page. Also the top half of the page looks good with the logo along top and good task bar also (we don’t like the spiel on left hand side covering up the picture + too many words!) If we could have our logo at lop like this along with our slogan which is 'Proud Standing Boughs that Thrive Strong'

http://www.wilmotgrovenurseries.co.nz/ - we like the bottom half of this with the clean lines and welcome to part down bottom rather than the spiel to the left as on above site. Also like the moving leaves, any chance we could have birds such as a fantail, Tui and Bellbirds flying across the page and also some birdsong playing?

This is their existing website, that needs an updated design: http://tallpineshade.co.nz/

Industry/Entity Type

It Company

Font styles to use
Serif
Sans Serif

Requirements
Must have
• "Website by Pagecraft Studio Co" located in bottom right hand side
Use images provided as background or banner images
Should not have
• Social Media icons

```html
<!DOCTYPE html>
<html lang="en">
<head>
<meta charset="utf-8">
<title>Tall Pine Shade</title>
<link href="https://fonts.googleapis.com/css2?family=Open+Sans:wght@400;600;700&family=Quicksand:wght@500;600;700&display=swap" rel="stylesheet">
<style>
:root{
  --header:#0a3a35;
  --footer:#0e5a5a;
  --teal:#0f6b68;
  --green:#138a3a;
  --yellow:#f7ec2b;
  --text:#555;
  --heading:#1d1d1d;
  --border:#d9d9d9;
  --white:#fff;
}
*{box-sizing:border-box;margin:0;padding:0}
html,body{width:879px;height:1200px;overflow:hidden}
body{position:relative;font-family:"Open Sans",sans-serif;background:var(--white);color:var(--text)}
.site-header{position:absolute;left:0;top:0;width:879px;height:94px;background:var(--header)}
.brand{position:absolute;left:76px;top:30px;display:flex;align-items:center;gap:8px;font-family:"Quicksand",sans-serif;font-weight:700;font-size:26px;color:var(--yellow)}
.brand-dot{width:14px;height:14px;border-radius:50%;background:var(--yellow)}
.contact-line{position:absolute;left:498px;top:14px;display:flex;align-items:center;gap:14px}
.phone{display:flex;align-items:center;gap:4px;color:var(--white);font-size:16px}
.slogan{color:var(--yellow);font-size:10px}
.main-nav{position:absolute;right:56px;top:51px;display:flex;gap:23px}
.main-nav a{color:var(--white);text-decoration:none;font-size:11.5px;font-weight:600}
.hero{position:absolute;left:0;top:94px;width:879px;height:440px;background:linear-gradient(180deg,#9bb8d6 0%,#c9d8e4 22%,#3f6330 45%,#2f4a22 65%,#8a8a82 85%,#b0ab9c 100%)}
.hero-caption{position:absolute;left:64px;top:151px;width:346px;height:126px;background:rgba(15,107,104,.85);border-radius:6px;padding:20px 22px;color:var(--white)}
.hero-caption h2{font-weight:600;font-size:18px;line-height:1.2}
.hero-caption h3{font-weight:400;font-size:24px;line-height:1.2}
.hero-caption p{font-size:9.5px;line-height:1.6;margin-top:6px;opacity:.9}
.hero-dots{position:absolute;left:416px;top:422px;display:flex;gap:3px}
.hero-dots span{width:9px;height:9px;border-radius:50%;background:#111}
.welcome{position:absolute;left:74px;top:570px;width:495px}
.welcome h1{font-family:"Quicksand",sans-serif;font-weight:500;font-size:20px;color:var(--heading);margin-bottom:8px}
.welcome p{font-size:9.8px;line-height:1.6;margin-bottom:12px}
.videos-title{position:absolute;left:72px;top:770px;font-family:"Quicksand",sans-serif;font-weight:600;font-size:18px;color:var(--teal)}
.video-main{position:absolute;left:74px;top:800px;width:328px;height:210px;border:1px solid var(--border);padding:5px;background:var(--white);box-shadow:0 1px 3px rgba(0,0,0,.1)}
.video-main .frame{width:100%;height:100%;background:linear-gradient(90deg,#6a5a48,#8b7a63 40%,#4f7fa5 55%,#6b5e50)}
.play{position:absolute;left:50%;top:50%;transform:translate(-50%,-50%)}
.thumb{position:absolute;left:410px;width:76px;height:48px;background:linear-gradient(180deg,#b7c9d8,#5e7350)}
.learn-more{position:absolute;left:70px;top:1027px;width:101px;height:28px;border:3px solid var(--yellow);border-radius:14px;background:var(--header);color:var(--white);font-size:9.5px;font-weight:600;display:flex;align-items:center;justify-content:center}
.bird{position:absolute;left:436px;top:1018px;width:137px;height:83px;background:linear-gradient(135deg,#f4f4f4,#d9e8a0 60%,#f4f4f4)}
.panel{position:absolute;left:598px;width:208px;border:1px solid var(--border);background:linear-gradient(180deg,#fff 60%,#f1f1f1)}
.panel h4{font-family:"Quicksand",sans-serif;font-weight:600;font-size:14px;color:var(--green)}
.search-panel{top:562px;height:74px;padding:12px 16px}
.search-field{margin-top:6px;height:22px;border:1px solid var(--border);background:var(--white);display:flex;align-items:center;justify-content:space-between;padding:0 6px;font-size:8.5px;font-style:italic;color:#888}
.gallery-panel{top:646px;height:196px}
.gallery-panel h4{padding:13px 19px 10px;border-bottom:1px solid var(--border)}
.gallery-panel ul{list-style:none;padding:10px 0 0 33px}
.gallery-panel li{font-size:9px;color:#444;line-height:19.4px;position:relative}
.gallery-panel li::before{content:"";position:absolute;left:-9px;top:7px;border-left:3px solid #333;border-top:3px solid transparent;border-bottom:3px solid transparent}
.info-panel{top:850px;height:210px;background:var(--white)}
.info-panel h4{background:var(--yellow);height:38px;padding:10px 18px}
.info-form{padding:11px 14px 0 17px}
.info-form .field{height:23px;border:1px solid var(--border);margin-bottom:6px;font-size:8.5px;color:#777;padding:5px 10px}
.submit{margin-top:3px;width:74px;height:25px;background:var(--teal);color:var(--white);font-size:9.5px;font-weight:700;display:flex;align-items:center;justify-content:center}
.site-footer{position:absolute;left:0;top:1101px;width:879px;height:99px;background:var(--footer);color:var(--white)}
.footer-nav{position:absolute;left:74px;top:28px;font-size:11px}
.footer-nav a{color:var(--white);text-decoration:none}
.footer-nav .sep{margin:0 6px}
.copyright{position:absolute;left:74px;top:56px;font-size:9px;opacity:.9}
.footer-brand{position:absolute;right:77px;top:28px;display:flex;align-items:center;gap:6px;font-family:"Quicksand",sans-serif;font-weight:700;font-size:18px;color:var(--yellow)}
.credit{position:absolute;right:78px;top:72px;font-size:9px;opacity:.9}
</style>
</head>
<body>
<header class="site-header">
  <div class="brand"><span class="brand-dot"></span>Tall Pine Shade</div>
  <div class="contact-line">
    <span class="phone">
      <svg width="14" height="14" viewBox="0 0 24 24"><path fill="#2fa39a" d="M6.6 10.8a15.1 15.1 0 0 0 6.6 6.6l2.2-2.2a1 1 0 0 1 1-.25 11.4 11.4 0 0 0 3.6.57 1 1 0 0 1 1 1V20a1 1 0 0 1-1 1A17 17 0 0 1 3 4a1 1 0 0 1 1-1h3.5a1 1 0 0 1 1 1c0 1.25.2 2.45.57 3.57a1 1 0 0 1-.25 1z"/></svg>
      555.304.7712
    </span>
    <span class="slogan">Proud Standing Boughs that Thrive Strong</span>
  </div>
  <nav class="main-nav">
    <a href="#">HOME</a><a href="#">ABOUT US</a><a href="#">TREE GALLERY</a><a href="#">PROJECTS</a><a href="#">CATALOGUE</a><a href="#">CONTACT</a>
  </nav>
</header>

<section class="hero" role="img" aria-label="Photo of a tree-lined road with tall conifers under a blue sky">
  <div class="hero-caption">
    <h2>Pellentesque faucibus accumsan</h2>
    <h3>Cras ante vitae enim iaculis</h3>
    <p>Aliquam nec erat at purus cursus interdum Vestibulum ligula augue bibendum accumsan vestibulum ut commodo Morbi</p>
  </div>
  <div class="hero-dots"><span></span><span></span><span></span><span></span></div>
</section>

<section class="welcome">
  <h1>Welcome to Tall Pine Shade Mainpage</h1>
  <p>Etiam eu urna Sed porta Suspendisse quam leo molestie sed luctus quis feugiat in pede Fusce tellus Sed metus augue convallis et vehicula ut pulvinar eu ante Integer orci tellus tristique vitae consequat nec porta vel lectus Nulla sit amet diam Duis non nunc libero a tempus libero lectus feugiat felis</p>
  <p>Etiam eu urna Sed porta Suspendisse quam leo molestie sed luctus quis feugiat in pede Fusce tellus Sed metus augue convallis et vehicula ut pulvinar eu ante Integer orci tellus tristique vitae consequat nec porta vel lectus Nulla sit amet diam Duis non nunc libero a tempus libero lectus feugiat felis Morbi diam mauris viverra in gravida eu mattis in ante Morbi eget arcu Morbi porta libero id ullamcorper nonummy nibh ligula</p>
</section>

<h2 class="videos-title">Watch Our Vidoes</h2>
<div class="video-main">
  <div class="frame" role="img" aria-label="Video still of a modern building with young trees in front"></div>
  <svg class="play" width="42" height="42" viewBox="0 0 42 42"><circle cx="21" cy="21" r="19" fill="#222" stroke="#fff" stroke-width="3"/><path d="M17 13l11 8-11 8z" fill="#fff"/></svg>
</div>
<div class="thumb" style="top:802px" role="img" aria-label="Video thumbnail of a building"><svg class="play" width="20" height="20" viewBox="0 0 20 20"><circle cx="10" cy="10" r="9" fill="#222" stroke="#fff" stroke-width="1.5"/><path d="M8 6l6 4-6 4z" fill="#fff"/></svg></div>
<div class="thumb" style="top:855px" role="img" aria-label="Video thumbnail of a road through hills"><svg class="play" width="20" height="20" viewBox="0 0 20 20"><circle cx="10" cy="10" r="9" fill="#222" stroke="#fff" stroke-width="1.5"/><path d="M8 6l6 4-6 4z" fill="#fff"/></svg></div>
<div class="thumb" style="top:910px" role="img" aria-label="Video thumbnail of mountains and houses"><svg class="play" width="20" height="20" viewBox="0 0 20 20"><circle cx="10" cy="10" r="9" fill="#222" stroke="#fff" stroke-width="1.5"/><path d="M8 6l6 4-6 4z" fill="#fff"/></svg></div>
<div class="thumb" style="top:964px" role="img" aria-label="Video thumbnail of a hillside"><svg class="play" width="20" height="20" viewBox="0 0 20 20"><circle cx="10" cy="10" r="9" fill="#222" stroke="#fff" stroke-width="1.5"/><path d="M8 6l6 4-6 4z" fill="#fff"/></svg></div>

<div class="learn-more">LEARN MORE</div>
<div class="bird" role="img" aria-label="Illustration of a green bellbird perched"></div>

<aside class="panel search-panel">
  <h4>Search Now</h4>
  <div class="search-field">Search here..
    <svg width="11" height="11" viewBox="0 0 12 12"><circle cx="5" cy="5" r="3.8" fill="none" stroke="#888" stroke-width="1.5"/><path d="M8 8l3 3" stroke="#888" stroke-width="1.6"/></svg>
  </div>
</aside>

<aside class="panel gallery-panel">
  <h4>Gallery Categories</h4>
  <ul>
    <li>Sed metus augue</li>
    <li>Convallis et ehicula pulvinar</li>
    <li>Ante Integer</li>
    <li>Orci tellus tristique</li>
    <li>Vitae consequat</li>
    <li>Nec porta vel lectus</li>
    <li>Nulla sit amet</li>
  </ul>
</aside>

<aside class="panel info-panel">
  <h4>Get More Information</h4>
  <div class="info-form">
    <div class="field">Your Name</div>
    <div class="field">Email address</div>
    <div class="field">Phone no.</div>
    <div class="field">City/Location</div>
    <div class="submit">SUBMIT</div>
  </div>
</aside>

<footer class="site-footer">
  <nav class="footer-nav">
    <a href="#">About Us</a><span class="sep">|</span><a href="#">Blog</a><span class="sep">|</span><a href="#">Catalogue</a><span class="sep">|</span><a href="#">Contact</a><span class="sep">|</span><a href="#">Product Galleries</a><span class="sep">|</span><a href="#">Projects</a>
  </nav>
  <p class="copyright">© 2013 Tall Pine Shade. All right reserved</p>
  <div class="footer-brand">Tall Pine Shade</div>
  <p class="credit">Website by Pagecraft Studio Co</p>
</footer>
</body>
</html>
```